Small Ecommerce Styled Site to Sell / Lease Domain Names

We have a small portfolio of 100+ domain names that we would like to offer for sale or lease via a web site. Along the lines of http://www.velramarkets.com/searchdomain.html?priceChoice=2&sort=leasing_desc

We would like initially a 4 page design, listing page (as site referenced above), domain info page (Universal Domain Name Landing Page with form) and checkout a page and About Us Page

We do not want a replica of the site listed, please use it as a guide only, we are looking for a fresh design, in similar concept web 2.0

Our Colours are #351a41 (Main) - #ffca27 (Secondary) all other colours must compliment those 2.
Updates

Domain Landing Page:  I am sorry I was not clear about expectations, however we would like a domain landing page that would be the default holding page for a domain name.

For some examples of what I mean please see:
https://www.pobexhub.com.au/guest-articles/7626-domain-for-sale-landing-pages.html
http://dev.quillterbrokers.com/blog/2013/09/sales-only-landers-and-buy-it-now-2/

Industry/Entity Type

Domain

Font styles to use
Sans Serif

```html
<!DOCTYPE html>
<html lang="en">
<head>
<meta charset="utf-8">
<title>Domain Leasing – Lease Domains</title>
<link href="https://fonts.googleapis.com/css2?family=Raleway:wght@400;500;600;700&display=swap" rel="stylesheet">
<style>
:root{
  --purple:#351a41;
  --purple-soft:#5a3a68;
  --yellow:#ffca27;
  --yellow-soft:#fdd66a;
  --yellow-deep:#e9b10f;
  --ink:#333;
  --muted:#777;
  --line:#d9d9d9;
  --panel:#e9e9e9;
  --row-alt:#f1f1f1;
  --cat-finance:#8c87c4;
  --cat-health:#e0505a;
  --cat-ent:#9b4fc0;
  --cat-home:#d98be3;
}
*{box-sizing:border-box;margin:0;padding:0}
html,body{width:1200px;height:2446px;overflow:hidden}
body{position:relative;background:#fff;font-family:'Raleway',sans-serif;color:var(--ink)}
a{color:inherit;text-decoration:none}
ul{list-style:none}

.topbar{position:absolute;left:0;top:0;width:1200px;height:41px;background:var(--purple);color:#fff;font-size:13px}
.topbar .promo{position:absolute;left:156px;top:13px}
.topbar .promo a{color:var(--yellow);margin-left:6px}
.topbar .util{position:absolute;right:156px;top:12px;display:flex;align-items:center;gap:10px;color:#c9a7d8}
.topbar .sep{width:1px;height:18px;background:#7a5a88}
.flag{display:inline-block;width:12px;height:9px;vertical-align:middle}

.header{position:absolute;left:0;top:41px;width:1200px;height:229px;background:linear-gradient(#fff,#e9e9e9)}
.logo{position:absolute;left:155px;top:37px;font-size:33px;font-weight:500;color:var(--purple);letter-spacing:.5px}
.btn-signup,.btn-login{position:absolute;top:37px;height:31px;width:84px;font-size:15px;text-align:center;line-height:31px;border-radius:2px}
.btn-signup{left:864px;background:var(--yellow);color:var(--purple)}
.btn-login{left:958px;background:var(--purple);color:var(--yellow)}

.mainnav{position:absolute;left:158px;top:145px;width:885px;height:46px;background:#fff;border:2px solid #ddd;display:flex;align-items:center;font-size:18px;color:var(--purple)}
.mainnav a{position:absolute;top:10px}
.mainnav .active{color:var(--yellow-deep);border-bottom:3px solid var(--yellow);padding-bottom:7px}
.mainnav .active::after{content:"";position:absolute;left:50%;bottom:-11px;margin-left:-8px;border:8px solid transparent;border-top-color:var(--yellow);border-bottom:0}

.searchband{position:absolute;left:155px;top:207px;width:888px;height:108px;background:linear-gradient(90deg,var(--yellow-soft),#fcd257)}
.search-input{position:absolute;left:21px;top:21px;width:375px;height:52px;background:#fff;border:4px solid #e0d3a7;font-size:21px;color:#bbb;font-style:italic;padding:10px 8px}
.search-btn{position:absolute;left:409px;top:21px;width:103px;height:54px;background:var(--purple);color:var(--yellow);font-size:21px;font-weight:600;text-align:center;line-height:54px;border-radius:2px}
.adv-search{position:absolute;left:21px;top:86px;font-size:14px;color:var(--purple)}
.tags{position:absolute;left:557px;top:18px;width:320px;font-size:14px;line-height:20px;color:var(--purple)}
.tags b{font-size:19px;font-weight:700}
.tags .y{color:#f0a90a}
.tags u{font-weight:600}

.sidebar{position:absolute;left:155px;width:215px}
.panel{position:absolute;left:155px;width:215px;background:var(--panel);padding:0 12px}
.panel h3{display:flex;align-items:center;gap:14px;font-size:21px;font-weight:500;color:var(--purple);height:46px;border-bottom:2px solid #fff}
.panel h3 svg{flex:none}
.cat-list{padding-top:10px;font-size:15px}
.cat-list li{height:24px;color:var(--purple);position:relative;padding-left:18px}
.cat-list li::before{content:"";position:absolute;left:2px;top:6px;border:4px solid transparent;border-left:5px solid var(--purple)}
.checks{display:grid;grid-template-columns:73px 73px 60px;row-gap:18px;padding-top:14px;font-size:13px;color:var(--purple)}
.checks label,.check-row{display:flex;align-items:center;gap:8px}
.box{width:16px;height:16px;background:#fff;border:1px solid #ccc;flex:none}
.minmax{display:flex;align-items:center;font-size:14px;color:var(--purple);padding-top:12px}
.minmax .field{width:53px;height:28px;background:#fff;border:1px solid #ccc;font-size:14px;color:#999;text-align:center;line-height:26px;margin:0 14px 0 5px}
.wordrow{display:flex;align-items:center;justify-content:space-between;font-size:13px;color:var(--purple);height:37px}
.wordrow .field{width:108px;height:26px;background:#fff;border:1px solid #ccc}
.lang-grid{display:grid;grid-template-columns:120px 80px;row-gap:19px;padding-top:14px;font-size:13px;color:var(--purple)}

.tabs{position:absolute;left:391px;top:341px;width:652px;font-size:15px;color:var(--purple)}
.tabs a{position:absolute;top:0}
.tabs .active{color:var(--yellow-deep);border-bottom:2px solid var(--yellow);padding-bottom:5px}
.tabs .order{right:0}
.listing{position:absolute;left:388px;top:368px;width:655px;height:1596px;border:1px solid var(--line);background:#fff}
.listing-meta{position:absolute;left:10px;top:10px;font-size:13px;color:var(--purple)}
.listing-nav{position:absolute;right:14px;top:10px;font-size:14px;color:var(--purple)}
.domains{position:absolute;left:0;top:47px;width:653px;border-collapse:collapse}
.domains th{height:27px;background:#e8e8e8;font-size:14px;font-weight:500;color:#777;text-align:left;border-top:1px solid var(--line);border-bottom:1px solid var(--line)}
.domains td{height:41px;font-size:14px}
.domains tr:nth-child(even) td{background:var(--row-alt)}
.domains .name{padding-left:10px;width:267px;font-weight:600;color:#222}
.domains .cat{font-size:13px;width:225px}
.c-fin{color:var(--cat-finance)}.c-hea{color:var(--cat-health)}.c-ent{color:var(--cat-ent)}.c-hom{color:var(--cat-home)}
.fee{display:inline-block;width:70px;height:24px;background:linear-gradient(#ffd84d,#f2b81a);border:1px solid #d9a20d;color:var(--purple);font-size:11px;font-weight:700;text-align:center;line-height:22px}
.offer{display:inline-block;width:69px;height:24px;background:var(--purple);color:var(--yellow);font-size:11px;font-weight:600;text-align:center;line-height:24px;margin-left:12px}

.pager{position:absolute;right:157px;top:1987px;font-size:14px;color:var(--purple)}
.pager b{color:var(--purple)}

.trust{position:absolute;left:264px;top:2037px;display:flex;gap:22px;align-items:center}
.trust span{display:block;height:38px;background:#cfcfcf;border-radius:4px}

.newsletter{position:absolute;left:0;top:2101px;width:1200px;height:57px;background:#e6e6e6;border-top:1px solid #d4d4d4}
.newsletter .icon{position:absolute;left:156px;top:9px}
.newsletter h2{position:absolute;left:222px;top:11px;font-size:27px;font-weight:600;color:var(--purple)}
.newsletter .email{position:absolute;left:549px;top:11px;width:366px;height:36px;background:#fff;border:1px solid #ccc;font-size:14px;color:#999;font-style:italic;padding:9px 10px}
.newsletter .subscribe{position:absolute;left:922px;top:11px;width:121px;height:36px;background:var(--purple);color:var(--yellow);font-size:18px;font-weight:600;text-align:center;line-height:36px}

.footer{position:absolute;left:0;top:2168px;width:1200px;height:212px;background:#ececec}
.fcol{position:absolute;top:13px;font-size:12px;color:#666;line-height:16px}
.fcol h4{font-size:13px;font-weight:500;color:var(--purple);margin-bottom:16px}
.fcol.divided{border-right:1px solid #ccc;height:185px}
.social{position:absolute;width:55px;height:55px}
.bottom{position:absolute;left:0;top:2380px;width:1200px;height:66px;background:#fff}
.bottom .copy{position:absolute;left:156px;top:28px;font-size:12px;color:#999}
.bottom .logo-foot{position:absolute;right:157px;top:20px;font-size:23px;font-weight:500;color:var(--purple)}
</style>
</head>
<body>

<div class="topbar">
  <div class="promo">Best In Price: <a href="#">ScriptDrillsheet.com</a></div>
  <div class="util">
    <svg width="16" height="14" viewBox="0 0 16 14"><path d="M1 1h3l2 8h8l1-6H5" fill="none" stroke="#c9a7d8" stroke-width="1.6"/><circle cx="7" cy="12" r="1.3" fill="#c9a7d8"/><circle cx="13" cy="12" r="1.3" fill="#c9a7d8"/></svg>
    <span>Cart (0)</span><span class="sep"></span><span>Language:</span>
    <span class="flag" style="background:#e30a17"></span><span class="flag" style="background:#3d4fa0"></span>
  </div>
</div>

<header class="header">
  <div class="logo">Domain Leasing</div>
  <a class="btn-signup" href="#">Sign Up</a>
  <a class="btn-login" href="#">Log In</a>
</header>

<nav class="mainnav">
  <a style="left:5px" href="#">Buy Domains</a>
  <a class="active" style="left:153px" href="#">Lease Domains</a>
  <a style="left:311px" href="#">Categories</a>
  <a style="left:432px" href="#">Valuation</a>
  <a style="left:539px" href="#">Affiliate</a>
  <a style="left:629px" href="#">FAQs</a>
  <a style="left:709px" href="#">Contact Us</a>
</nav>

<section class="searchband">
  <div class="search-input">Enter Keyword or Domain</div>
  <a class="search-btn" href="#">Search</a>
  <div class="adv-search">Advanced Search &nbsp;&rarr;</div>
  <div class="tags">
    <b>New</b> Added Domains <b>Hot</b> Prices <span class="y">Games</span><br>
    <span class="y">Entertainment</span> Domains <u>Business Domains</u><br>
    <u>Tech</u> Domains <span class="y">Medical</span> Domains <b style="font-size:14px">Life Style</b>
  </div>
</section>

<aside>
  <div class="panel" style="top:334px;height:400px">
    <h3><svg width="24" height="22" viewBox="0 0 24 22"><rect x="1" y="1" width="22" height="20" rx="2" fill="var(--purple)"/><rect x="5" y="5" width="14" height="3" fill="#fff"/></svg>Categories</h3>
    <ul class="cat-list">
      <li>Automotive</li><li>Business and Finance</li><li>Computers and Internet</li><li>Education</li><li>Entertainment</li><li>Family</li><li>Food and Beverage</li><li>Games</li><li>Home and Garden</li><li>Health and Beauty</li><li>Lifestyle</li><li>Shopping</li><li>Travel</li><li>Sports</li>
    </ul>
  </div>

  <div class="panel" style="top:753px;height:171px">
    <h3><svg width="22" height="22" viewBox="0 0 22 22"><rect x="2" y="2" width="18" height="5" fill="var(--purple)"/><rect x="2" y="9" width="18" height="5" fill="var(--purple)"/><rect x="2" y="16" width="18" height="5" fill="var(--purple)"/></svg>Extensions</h3>
    <div class="checks">
      <label><span class="box"></span>All</label><label><span class="box"></span>.com</label><label><span class="box"></span>.net</label>
      <label><span class="box"></span>.info</label><label><span class="box"></span>.org</label><label><span class="box"></span>.es</label>
      <label><span class="box"></span>.co.za</label><label><span class="box"></span>.co.uk</label><label><span class="box"></span>.de</label>
    </div>
  </div>

  <div class="panel" style="top:942px;height:96px">
    <h3><svg width="24" height="24" viewBox="0 0 24 24"><path d="M2 11L12 2l10 9v11H2z" fill="var(--purple)"/><text x="12" y="19" font-size="10" fill="#fff" text-anchor="middle" font-family="Raleway,sans-serif" font-weight="700">$</text></svg>Price Range</h3>
    <div class="minmax">Min:<span class="field">0</span>Max:<span class="field">0</span></div>
  </div>

  <div class="panel" style="top:1056px;height:95px">
    <h3><svg width="28" height="16" viewBox="0 0 28 16"><rect x="1" y="2" width="26" height="12" fill="none" stroke="var(--purple)" stroke-width="2.5"/><path d="M7 2v6M12 2v4M17 2v6M22 2v4" stroke="var(--purple)" stroke-width="2"/></svg>Length</h3>
    <div class="minmax">Min:<span class="field">0</span>Max:<span class="field">0</span></div>
  </div>

  <div class="panel" style="top:1170px;height:95px">
    <h3><svg width="20" height="24" viewBox="0 0 20 24"><rect x="1" y="1" width="18" height="22" rx="2" fill="none" stroke="var(--purple)" stroke-width="2.5"/><path d="M5 7h10M5 12h10M5 17h6" stroke="var(--purple)" stroke-width="2"/></svg>Word Count</h3>
    <div class="minmax">Min:<span class="field">0</span>Max:<span class="field">0</span></div>
  </div>

  <div class="panel" style="top:1284px;height:216px">
    <h3><svg width="24" height="24" viewBox="0 0 24 24"><circle cx="5" cy="12" r="4" fill="var(--purple)"/><circle cx="19" cy="5" r="4" fill="var(--purple)"/><circle cx="19" cy="19" r="4" fill="var(--purple)"/><path d="M5 12L19 5M5 12l14 7" stroke="var(--purple)" stroke-width="2.5"/></svg>Word Structure</h3>
    <div style="padding-top:6px">
      <div class="wordrow">Begins With:<span class="field"></span></div>
      <div class="wordrow">Ends With:<span class="field"></span></div>
      <div class="wordrow">Exclude:<span class="field"></span></div>
      <div class="check-row" style="font-size:13px;color:var(--purple);height:29px"><span class="box"></span>Disallow Hyphen</div>
      <div class="check-row" style="font-size:13px;color:var(--purple);height:29px"><span class="box"></span>Disallow Number</div>
    </div>
  </div>

  <div class="panel" style="top:1519px;height:219px">
    <h3><svg width="26" height="26" viewBox="0 0 26 26"><circle cx="13" cy="13" r="12" fill="var(--purple)"/><path d="M8 6c3 2 2 5 5 6s2 5 0 8M16 4c-1 3 2 4 5 5" stroke="#fff" stroke-width="2" fill="none"/></svg>Language</h3>
    <div class="lang-grid">
      <label class="check-row"><span class="box"></span>All</label><label class="check-row"><span class="box"></span>English</label>
      <label class="check-row"><span class="box"></span>Spanish</label><label class="check-row"><span class="box"></span>German</label>
      <label class="check-row"><span class="box"></span>French</label><label class="check-row"><span class="box"></span>Turkish</label>
      <label class="check-row"><span class="box"></span>Italian</label><label class="check-row"><span class="box"></span>Dutch</label>
    </div>
  </div>
</aside>

<div class="tabs">
  <a style="left:0" href="#">All Domains</a>
  <a style="left:106px" href="#">Buy Domains</a>
  <a class="active" style="left:223px" href="#">List Domains</a>
  <a class="order" href="#">Select Order &nbsp;&#9662;</a>
</div>

<main class="listing">
  <div class="listing-meta">Displaying <b>1 - 75</b> of <b>63280</b> Domains</div>
  <div class="listing-nav">Next &nbsp;&rsaquo; &nbsp;|&nbsp; Last &raquo;</div>
  <table class="domains">
    <thead><tr><th style="padding-left:10px">Domain Name</th><th>Category</th><th style="padding-left:8px">Lease Fee</th><th style="padding-left:24px">Price</th></tr></thead>
    <tbody>
      <tr><td class="name">ScoreHarbor.com</td><td class="cat c-fin">Business &amp; Finance</td><td><span class="fee">$15,500</span></td><td><span class="offer">Make offer</span></td></tr>
      <tr><td class="name">SlimShiftly.com</td><td class="cat c-hea">Health &amp; Beauty</td><td><span class="fee">$15,500</span></td><td><span class="offer">Make offer</span></td></tr>
      <tr><td class="name">WaveCastly.com</td><td class="cat c-ent">Entertainment</td><td><span class="fee">$15,500</span></td><td><span class="offer">Make offer</span></td></tr>
      <tr><td class="name">RooftopRenewly.com</td><td class="cat c-hom">Home &amp; Garden</td><td><span class="fee">$15,500</span></td><td><span class="offer">Make offer</span></td></tr>
      <tr><td class="name">ScoreHarbor.com</td><td class="cat c-fin">Business &amp; Finance</td><td><span class="fee">$15,500</span></td><td><span class="offer">Make offer</span></td></tr>
      <tr><td class="name">SlimShiftly.com</td><td class="cat c-hea">Health &amp; Beauty</td><td><span class="fee">$15,500</span></td><td><span class="offer">Make offer</span></td></tr>
      <tr><td class="name">WaveCastly.com</td><td class="cat c-fin">Business &amp; Finance</td><td><span class="fee">$15,500</span></td><td><span class="offer">Make offer</span></td></tr>
      <tr><td class="name">RooftopRenewly.com</td><td class="cat c-hea">Health &amp; Beauty</td><td><span class="fee">$15,500</span></td><td><span class="offer">Make offer</span></td></tr>
      <tr><td class="name">ScoreHarbor.com</td><td class="cat c-fin">Business &amp; Finance</td><td><span class="fee">$15,500</span></td><td><span class="offer">Make offer</span></td></tr>
      <tr><td class="name">SlimShiftly.com</td><td class="cat c-hea">Health &amp; Beauty</td><td><span class="fee">$15,500</span></td><td><span class="offer">Make offer</span></td></tr>
      <tr><td class="name">WaveCastly.com</td><td class="cat c-ent">Entertainment</td><td><span class="fee">$15,500</span></td><td><span class="offer">Make offer</span></td></tr>
      <tr><td class="name">RooftopRenewly.com</td><td class="cat c-hom">Home &amp; Garden</td><td><span class="fee">$15,500</span></td><td><span class="offer">Make offer</span></td></tr>
      <tr><td class="name">ScoreHarbor.com</td><td class="cat c-fin">Business &amp; Finance</td><td><span class="fee">$15,500</span></td><td><span class="offer">Make offer</span></td></tr>
      <tr><td class="name">SlimShiftly.com</td><td class="cat c-hea">Health &amp; Beauty</td><td><span class="fee">$15,500</span></td><td><span class="offer">Make offer</span></td></tr>
      <tr><td class="name">WaveCastly.com</td><td class="cat c-fin">Business &amp; Finance</td><td><span class="fee">$15,500</span></td><td><span class="offer">Make offer</span></td></tr>
      <tr><td class="name">SlimShiftly.com</td><td class="cat c-hea">Health &amp; Beauty</td><td><span class="fee">$15,500</span></td><td><span class="offer">Make offer</span></td></tr>
      <tr><td class="name">WaveCastly.com</td><td class="cat c-ent">Entertainment</td><td><span class="fee">$15,500</span></td><td><span class="offer">Make offer</span></td></tr>
      <tr><td class="name">RooftopRenewly.com</td><td class="cat c-hom">Home &amp; Garden</td><td><span class="fee">$15,500</span></td><td><span class="offer">Make offer</span></td></tr>
      <tr><td class="name">ScoreHarbor.com</td><td class="cat c-fin">Business &amp; Finance</td><td><span class="fee">$15,500</span></td><td><span class="offer">Make offer</span></td></tr>
      <tr><td class="name">SlimShiftly.com</td><td class="cat c-hea">Health &amp; Beauty</td><td><span class="fee">$15,500</span></td><td><span class="offer">Make offer</span></td></tr>
      <tr><td class="name">WaveCastly.com</td><td class="cat c-fin">Business &amp; Finance</td><td><span class="fee">$15,500</span></td><td><span class="offer">Make offer</span></td></tr>
      <tr><td class="name">RooftopRenewly.com</td><td class="cat c-hea">Health &amp; Beauty</td><td><span class="fee">$15,500</span></td><td><span class="offer">Make offer</span></td></tr>
      <tr><td class="name">ScoreHarbor.com</td><td class="cat c-fin">Business &amp; Finance</td><td><span class="fee">$15,500</span></td><td><span class="offer">Make offer</span></td></tr>
      <tr><td class="name">SlimShiftly.com</td><td class="cat c-hea">Health &amp; Beauty</td><td><span class="fee">$15,500</span></td><td><span class="offer">Make offer</span></td></tr>
      <tr><td class="name">WaveCastly.com</td><td class="cat c-fin">Business &amp; Finance</td><td><span class="fee">$15,500</span></td><td><span class="offer">Make offer</span></td></tr>
      <tr><td class="name">RooftopRenewly.com</td><td class="cat c-hea">Health &amp; Beauty</td><td><span class="fee">$15,500</span></td><td><span class="offer">Make offer</span></td></tr>
      <tr><td class="name">WaveCastly.com</td><td class="cat c-fin">Business &amp; Finance</td><td><span class="fee">$15,500</span></td><td><span class="offer">Make offer</span></td></tr>
      <tr><td class="name">RooftopRenewly.com</td><td class="cat c-hea">Health &amp; Beauty</td><td><span class="fee">$15,500</span></td><td><span class="offer">Make offer</span></td></tr>
      <tr><td class="name">WaveCastly.com</td><td class="cat c-fin">Business &amp; Finance</td><td><span class="fee">$15,500</span></td><td><span class="offer">Make offer</span></td></tr>
      <tr><td class="name">RooftopRenewly.com</td><td class="cat c-hea">Health &amp; Beauty</td><td><span class="fee">$15,500</span></td><td><span class="offer">Make offer</span></td></tr>
      <tr><td class="name">WaveCastly.com</td><td class="cat c-fin">Business &amp; Finance</td><td><span class="fee">$15,500</span></td><td><span class="offer">Make offer</span></td></tr>
      <tr><td class="name">RooftopRenewly.com</td><td class="cat c-hea">Health &amp; Beauty</td><td><span class="fee">$15,500</span></td><td><span class="offer">Make offer</span></td></tr>
      <tr><td class="name">WaveCastly.com</td><td class="cat c-fin">Business &amp; Finance</td><td><span class="fee">$15,500</span></td><td><span class="offer">Make offer</span></td></tr>
      <tr><td class="name">RooftopRenewly.com</td><td class="cat c-hea">Health &amp; Beauty</td><td><span class="fee">$15,500</span></td><td><span class="offer">Make offer</span></td></tr>
      <tr><td class="name">WaveCastly.com</td><td class="cat c-fin">Business &amp; Finance</td><td><span class="fee">$15,500</span></td><td><span class="offer">Make offer</span></td></tr>
      <tr><td class="name">RooftopRenewly.com</td><td class="cat c-hea">Health &amp; Beauty</td><td><span class="fee">$15,500</span></td><td><span class="offer">Make offer</span></td></tr>
    </tbody>
  </table>
</main>

<div class="pager"><b>1</b> | 2 | 3 | 4 | 5 | 6 | 7 | ... | Next &rsaquo; | Last &nbsp;&raquo;</div>

<div class="trust" role="img" aria-label="Payment and security badges">
  <span style="width:84px"></span><span style="width:55px"></span><span style="width:68px"></span>
  <span style="width:98px"></span><span style="width:76px"></span><span style="width:100px"></span><span style="width:52px;border-radius:50%"></span>
</div>

<section class="newsletter">
  <svg class="icon" width="41" height="38" viewBox="0 0 41 38"><rect width="41" height="38" fill="var(--purple)"/><rect x="7" y="10" width="27" height="18" fill="none" stroke="#fff" stroke-width="2"/><path d="M7 10l13.5 11L34 10M7 28l10-9M34 28l-10-9" fill="none" stroke="#fff" stroke-width="2"/></svg>
  <h2>Sign Up For Newsletter</h2>
  <div class="email">Enter your Email Address</div>
  <a class="subscribe" href="#">Subscribe</a>
</section>

<footer class="footer">
  <div class="fcol divided" style="left:158px;width:185px">
    <h4>About Domain Leased</h4>
    News<br>Blog<br>FAQ<br>Success Stories<br>Membership Contract<br>Privacy Policy<br>Success Stories<br>Membership Contract<br>Privacy Policy
  </div>
  <div class="fcol divided" style="left:372px;width:158px">
    <h4>Buy Domains</h4>
    Premium Domains<br>Bargain Domains<br>Popular Domains<br>Top keyword
  </div>
  <div class="fcol" style="left:556px;width:190px">
    <h4>Categories</h4>
    Automotive<br>Business and Finance<br>Computers and Internet<br>Education<br>Entertainment<br>Family<br>Food and Beverage<br>Games<br>Home and Garden
  </div>
  <div class="fcol divided" style="left:751px;width:150px;padding-top:32px">
    Health and Beauty<br>Lifestyle<br>Shopping<br>Travel<br>Sports
  </div>
  <div class="fcol" style="left:922px">
    <h4>Follow Us</h4>
  </div>
  <span class="social" style="left:922px;top:49px;background:#5a9bd5" role="img" aria-label="Social profile link"></span>
  <span class="social" style="left:988px;top:49px;background:#3f5a9a" role="img" aria-label="Social profile link"></span>
  <span class="social" style="left:922px;top:114px;background:#1177b0" role="img" aria-label="Social profile link"></span>
  <span class="social" style="left:988px;top:114px;background:#ef8f2a" role="img" aria-label="News feed link"></span>
</footer>

<div class="bottom">
  <div class="copy">Copyright @ 2014 - Domain Leasing</div>
  <div class="logo-foot">Domain Leasing</div>
</div>

</body>
</html>
```